Harrowgate Estates Business Card for Apartment Buildings

Create business cards for resident managers who run apartment buildings. The audience is the public who are searching for apartment rentals, and current residents who live at the apartment building. Key design element will be incorporating the company logo, however, the logo cannot dominate. The building name and manager name are more important than the logo. Current business card design leaves little room for copy, so we may need to reduce the size on the current card to allow for more space for copy.

Target Market(s)

Adults 18-65 years of age, who are looking for an apartment rental, plus current residents who live at our apartment buildings.

Industry/Entity Type

Property Management

Contact Information for Business Card

A major design element will be use of the company logo. Important property and manager contact information must be part of the design. The size of the logo will need to be reduced to make room for building and manager contact copy.

Font styles to use
Sans Serif

Colors
3176b5
000000
959595
ffffff

Requirements
Must have
• 1) Incorporate the company logo.
• 2) Use the company colors (dark blue, black/grey, over white).
• 3) FEATURE THE BUILDING NAME
• 4) FEATURE THE MANAGER NAME
• 5) The company name is less important than BUILDING and MANAGER
• 6) Manager contact information
• **SEE ATTACHED CREATIVE BRIEF**
Nice to have
• 1) Back of card logo watermark
• 2) Ability to write notes on back of carfd
Should not have
• Avoid letting the company logo dominate the card, the building name and manager are more important than the company logo.

```html
<!DOCTYPE html>
<html lang="en">
<head>
<meta charset="utf-8">
<title>Harrowgate Estates – Resident Manager Business Card</title>
<link href="https://fonts.googleapis.com/css2?family=Red+Hat+Display:wght@500;600;700&display=swap" rel="stylesheet">
<style>
  :root {
    --brand-blue: #0a6aa8;
    --ink: #3a3a3a;
    --grey: #959595;
    --paper: #ffffff;
    --stage: #ececec;
    --dot: #555555;
  }
  * { box-sizing: border-box; margin: 0; padding: 0; }
  html, body { width: 1200px; height: 1200px; overflow: hidden; }
  body {
    background: var(--stage);
    font-family: "Red Hat Display", Arial, sans-serif;
    color: var(--ink);
    position: relative;
  }
  .card {
    position: absolute;
    left: 206px;
    width: 787px;
    height: 462px;
    background: var(--paper);
    overflow: hidden;
  }
  .card--front { top: 88px; border-bottom: 2px solid var(--brand-blue); }
  .card--back { top: 646px; }

  /* Brand name block */
  .brand {
    position: absolute;
    display: flex;
    align-items: center;
    gap: 10px;
    font-weight: 700;
    line-height: 1;
    white-space: nowrap;
  }
  .brand__dot { border-radius: 50%; flex: none; }
  .card--front .brand { left: 30px; top: 226px; color: var(--brand-blue); font-size: 28px; }
  .card--front .brand__dot { width: 26px; height: 26px; background: var(--brand-blue); }

  .divider {
    position: absolute;
    left: 392px; top: 60px;
    width: 2px; height: 218px;
    background: var(--ink);
  }

  .manager { position: absolute; left: 411px; top: 54px; }
  .manager__name { font-size: 32px; font-weight: 700; color: var(--brand-blue); line-height: 1.1; }
  .manager__title { font-size: 18px; font-weight: 500; color: var(--ink); margin-top: 2px; }

  .contacts { position: absolute; left: 409px; top: 124px; list-style: none; }
  .contacts li {
    display: flex; align-items: center; gap: 12px;
    height: 31.5px;
    font-size: 19px; font-weight: 500; color: var(--ink);
  }
  .contacts svg { width: 24px; height: 24px; flex: none; }

  .property { position: absolute; left: 0; right: 0; top: 336px; text-align: center; }
  .property__name { font-size: 30px; font-weight: 700; color: var(--brand-blue); }
  .property__address { font-size: 18px; font-weight: 600; color: var(--ink); margin-top: 6px; }

  /* Back */
  .back__header {
    position: absolute; left: 0; top: 0;
    width: 100%; height: 144px;
    background: var(--brand-blue);
  }
  .card--back .brand { left: 50%; top: 54px; transform: translateX(-50%); color: var(--paper); font-size: 38px; }
  .card--back .brand__dot { width: 32px; height: 32px; background: var(--paper); }

  .notes { position: absolute; left: 29px; right: 31px; top: 143px; }
  .notes__line {
    height: 30.8px;
    border-bottom: 3px dotted var(--dot);
    display: flex; align-items: flex-end;
  }
  .notes__label {
    font-size: 22px; font-weight: 600; color: var(--ink);
    background: var(--paper); padding-right: 6px; margin-bottom: -6px; line-height: 1;
  }
  .back__footer {
    position: absolute; left: 0; bottom: 0;
    width: 100%; height: 29px;
    background: var(--brand-blue);
  }
</style>
</head>
<body>

<section class="card card--front" aria-label="Business card front">
  <div class="brand"><span class="brand__dot"></span>Harrowgate Estates</div>
  <div class="divider"></div>

  <div class="manager">
    <h1 class="manager__name">Marisol Delgado</h1>
    <p class="manager__title">Resident Manager</p>
  </div>

  <ul class="contacts">
    <li>
      <svg viewBox="0 0 24 24" aria-label="Office phone"><circle cx="12" cy="12" r="12" fill="var(--brand-blue)"/><path d="M8.2 6.5c.6-.4 1.2-.2 1.5.3l1 1.8c.3.5.1 1-.3 1.3l-.7.5c.5 1.3 1.6 2.4 2.9 3l.5-.7c.3-.4.9-.6 1.3-.3l1.8 1c.5.3.7.9.3 1.5-.8 1.2-2 1.6-3.2 1.1-2.7-1.1-4.8-3.2-5.9-5.9-.5-1.2-.1-2.4 1-3.1z" fill="#fff"/></svg>
      555-301-4827
    </li>
    <li>
      <svg viewBox="0 0 24 24" aria-label="Mobile phone"><circle cx="12" cy="12" r="12" fill="var(--brand-blue)"/><rect x="8.5" y="5.5" width="7" height="13" rx="1.5" fill="#fff"/><rect x="9.8" y="7.2" width="4.4" height="8.6" fill="var(--brand-blue)"/></svg>
      555-418-2093
    </li>
    <li>
      <svg viewBox="0 0 24 24" aria-label="Fax"><circle cx="12" cy="12" r="12" fill="var(--brand-blue)"/><rect x="8.5" y="5.5" width="7" height="4" fill="#fff"/><rect x="6" y="10" width="12" height="6" rx="1" fill="#fff"/><rect x="8.5" y="13.5" width="7" height="5" fill="#fff" stroke="var(--brand-blue)" stroke-width="1"/></svg>
      555-672-3150
    </li>
    <li>
      <svg viewBox="0 0 24 24" aria-label="Email"><circle cx="12" cy="12" r="12" fill="var(--brand-blue)"/><rect x="6.5" y="8" width="11" height="8.5" rx="1" fill="#fff"/><path d="M6.8 8.5 12 12.5l5.2-4" fill="none" stroke="var(--brand-blue)" stroke-width="1.4"/></svg>
      marisol@harrowgate.com
    </li>
    <li>
      <svg viewBox="0 0 24 24" aria-label="Website"><circle cx="12" cy="12" r="12" fill="var(--brand-blue)"/><circle cx="12" cy="12" r="6" fill="none" stroke="#fff" stroke-width="1.5"/><ellipse cx="12" cy="12" rx="2.6" ry="6" fill="none" stroke="#fff" stroke-width="1.2"/><path d="M6 12h12" stroke="#fff" stroke-width="1.2"/></svg>
      www.harrowgate.com
    </li>
  </ul>

  <div class="property">
    <h2 class="property__name">Cedar Court Apartments</h2>
    <p class="property__address">1482 Linden Avenue, Fairview, CA 90417</p>
  </div>
</section>

<section class="card card--back" aria-label="Business card back">
  <header class="back__header">
    <div class="brand"><span class="brand__dot"></span>Harrowgate Estates</div>
  </header>

  <div class="notes">
    <div class="notes__line"><span class="notes__label">Write Notes :</span></div>
    <div class="notes__line"></div>
    <div class="notes__line"></div>
    <div class="notes__line"></div>
    <div class="notes__line"></div>
    <div class="notes__line"></div>
    <div class="notes__line"></div>
    <div class="notes__line"></div>
    <div class="notes__line"></div>
  </div>

  <footer class="back__footer"></footer>
</section>

</body>
</html>
```